BrivoMatex. Lantern for the Steady Growth. Business card

Professional business card for BrivoMatex (Lantern for the Steady Growth)
My rationale: Strategy-> Execution-> Results-> Value that lead to the BrivoMatex name: We put the Lantern for the Steady Growth.
We deliver value to our customers helping them at defining a good strategy (cyan arrow). 90% of well formulated strategies fail due to poor execution so we also consider strategical execution very important (green arrow). Due to the execution we obtain the results (blue arrow). Finally, the results provide feedback to redefine strategy, and the new strategy has to be executed and new results obtained providing new feedback and on and on. It's like a wheel that finally, must create corporate value: value for shareholders, staholders, employees, providers...-

Target Market(s)

CEOs and steering comitees , invewrnent funds

Industry/Entity Type

Business Consultant

Contact Information for Business Card

Tommaso Ferlini
CEO & Founder
tommaso.ferlini@brivomatex.example
Mobile: +34 611.205.938
www.brivomatex.example

Colors

Designer to choose colors to be used in the design.

Requirements
Nice to have
• Nice to hace the words: Strategy, execution, results
• Nice to vave the claim: Lantern for the Steady Growth
• The three colors should be shown:
• cyan for STRATEGY
• green for EXECUTION
• blue for RESULTS
Should not have
• Complete black background

```html
<!DOCTYPE html>
<html lang="en">
<head>
<meta charset="utf-8">
<title>BrivoMatex – Business Card</title>
<link rel="stylesheet" href="https://fonts.googleapis.com/css2?family=Lato:wght@400;700;900&display=swap">
<style>
  :root {
    --page-bg: #dedede;
    --card-front: #ffffff;
    --card-back: #161b2e;
    --navy: #253a8f;
    --brand-on-dark: #3a52b8;
    --grey-text: #8a8a8a;
    --claim-text: #aab0c4;
    --cyan: #29abe2;
    --green: #8dc63f;
    --blue: #4a5fc1;
  }
  * { box-sizing: border-box; margin: 0; padding: 0; }
  html, body {
    width: 1200px; height: 960px; overflow: hidden;
    background: var(--page-bg);
    font-family: "Lato", sans-serif;
  }
  .canvas { position: relative; width: 1200px; height: 960px; }
  .card {
    position: absolute; left: 281px; width: 655px; height: 373px;
    border-radius: 26px; overflow: hidden;
    box-shadow: 0 3px 3px rgba(0, 0, 0, 0.35);
  }
  .card--front { top: 81px; background: var(--card-front); }
  .card--back { top: 506px; background: var(--card-back); }

  .brand-name {
    position: absolute; font-family: "Lato", sans-serif;
    font-weight: 900; letter-spacing: -0.5px; white-space: nowrap; line-height: 1;
  }
  .card--front .brand-name { right: 60px; top: 138px; font-size: 37px; color: var(--navy); }
  .card--back .brand-name {
    left: 0; right: 0; text-align: center; top: 202px; font-size: 52px; color: var(--brand-on-dark);
  }

  .holder { position: absolute; left: 64px; top: 172px; }
  .holder__name { font-size: 27px; font-weight: 700; color: var(--navy); line-height: 1.2; }
  .holder__role { font-size: 17.5px; color: var(--grey-text); margin-top: 2px; }

  .contacts { position: absolute; left: 64px; top: 247px; list-style: none; }
  .contacts__item {
    display: flex; align-items: center; gap: 8px;
    font-size: 17px; color: var(--grey-text); height: 24px;
  }
  .contacts__icon { width: 15px; height: 15px; flex: none; }

  .tagline {
    position: absolute; left: 0; right: 0; top: 282px;
    text-align: center; font-size: 17.5px; color: #888; letter-spacing: 0.3px;
  }
  .tagline__strategy { color: var(--cyan); }
  .tagline__execution { color: var(--green); }
  .tagline__results { color: var(--blue); }
  .tagline__sep { margin: 0 6px; }

  .claim {
    position: absolute; left: 0; right: 0; top: 314px;
    text-align: center; font-size: 13px; font-style: italic;
    color: var(--claim-text); letter-spacing: 0.4px;
  }
</style>
</head>
<body>
<main class="canvas">
  <section class="card card--front">
    <div class="brand-name">BrivoMatex</div>
    <div class="holder">
      <h1 class="holder__name">Tommaso Ferlini</h1>
      <p class="holder__role">CEO &amp; Founder</p>
    </div>
    <ul class="contacts">
      <li class="contacts__item">
        <svg class="contacts__icon" viewBox="0 0 16 16"><path d="M3 14 C3 8 7 3 13 2 L14 5 L11 6 C8 7 6 10 6 13 Z" fill="var(--navy)"/></svg>
        +34 611.205.938
      </li>
      <li class="contacts__item">
        <svg class="contacts__icon" viewBox="0 0 16 16"><rect x="1" y="4" width="14" height="9" fill="var(--navy)"/><path d="M1 4 L8 10 L15 4" stroke="#fff" stroke-width="1.3" fill="none"/></svg>
        tommaso.ferlini@brivomatex.example
      </li>
      <li class="contacts__item">
        <svg class="contacts__icon" viewBox="0 0 16 16" fill="none" stroke="var(--navy)" stroke-width="1.3"><circle cx="8" cy="8" r="6.5"/><ellipse cx="8" cy="8" rx="3" ry="6.5"/><path d="M1.5 8 H14.5 M2.5 4.8 H13.5 M2.5 11.2 H13.5"/></svg>
        www.brivomatex.example
      </li>
    </ul>
  </section>

  <section class="card card--back">
    <div class="brand-name">BrivoMatex</div>
    <p class="tagline">
      <span class="tagline__strategy">STRATEGY</span><span class="tagline__sep">-</span><span class="tagline__execution">EXECUTION</span><span class="tagline__sep">-</span><span class="tagline__results">RESULTS</span>
    </p>
    <p class="claim">Lantern for the Steady Growth</p>
  </section>
</main>
</body>
</html>
```